KVT Business Cards

We require business cards for our business. We would like a matte black back to the card, with our logo centred in the middle. The front side of the card is open to design.

Target Market(s)

Clients looking for legal services (professional)

Industry/Entity Type

Legal

Contact Information for Business Card

Boris Telemark
Partner
Mobile: 0438 715 642
Email: boris@kvtlaw.co
Website: www.kvtlaw.co
Level 3, 118 Wexbury Street
Sydney NSW 2000

Font styles to use
Other font styles liked:
• Avenir

Colors
f04a50
ffffff
1b1b1b

Requirements
Must have
• Black back with logo included in the centre of the card.
• Our font is Avenir.

```html
<!DOCTYPE html>
<html lang="en">
<head>
<meta charset="utf-8">
<title>KVT Business Cards</title>
<link href="https://fonts.googleapis.com/css2?family=Nunito+Sans:wght@400;600;700;800&display=swap" rel="stylesheet">
<style>
  :root {
    --backdrop: #3f3f3f;
    --card-black: #0b0b0b;
    --brand-red: #e8101a;
    --brand-red-deep: #9c1219;
    --logo-red: #d4102e;
    --white: #ffffff;
  }
  * { margin: 0; padding: 0; box-sizing: border-box; }
  html, body { width: 1200px; height: 1200px; overflow: hidden; }
  body {
    background: radial-gradient(circle at 50% 50%, #545454 0%, var(--backdrop) 70%);
    font-family: "Nunito Sans", sans-serif;
    color: var(--white);
    position: relative;
  }
  .card {
    position: absolute;
    background: radial-gradient(circle at 55% 45%, #1c1c1c 0%, var(--card-black) 70%);
    overflow: hidden;
  }
  .card-front { left: 116px; top: 28px; width: 978px; height: 558px; }
  .card-back  { left: 116px; top: 621px; width: 972px; height: 555px; }

  .band { position: absolute; }
  .band-top {
    right: 0; top: 0; width: 420px; height: 40px;
    background: linear-gradient(90deg, var(--brand-red), var(--brand-red-deep));
  }
  .band-bottom {
    left: 0; bottom: 0; width: 420px; height: 40px;
    background: linear-gradient(90deg, var(--brand-red-deep), var(--brand-red));
  }
  .rule {
    position: absolute; height: 3px; background: var(--brand-red);
  }
  .rule-upper { left: 0; top: 238px; width: 300px; }
  .rule-lower { right: 0; top: 330px; width: 300px; }

  .brand {
    position: absolute;
    display: flex;
    align-items: center;
    gap: 14px;
  }
  .brand-square { background: var(--logo-red); flex: none; }
  .brand-name {
    font-weight: 800;
    color: var(--white);
    text-transform: uppercase;
    line-height: 1.08;
    letter-spacing: 0.2px;
  }
  .card-front .brand { left: 700px; top: 128px; }
  .card-front .brand-square { width: 18px; height: 18px; }
  .card-front .brand-name { font-size: 21px; }
  .card-back .brand { left: 50%; top: 50%; transform: translate(-50%, -50%); gap: 20px; }
  .card-back .brand-square { width: 28px; height: 28px; }
  .card-back .brand-name { font-size: 30px; }

  .contact-list { position: absolute; left: 46px; top: 290px; list-style: none; }
  .contact-item {
    display: flex;
    align-items: flex-start;
    font-size: 16.5px;
    line-height: 20px;
    margin-bottom: 16px;
  }
  .contact-item:nth-child(1) { margin-bottom: 19px; }
  .contact-item:nth-child(2) { margin-bottom: 17px; }
  .contact-item:nth-child(3) { margin-bottom: 14px; }
  .contact-icon { width: 24px; height: 24px; margin-right: 13px; flex: none; margin-top: -2px; }
  .contact-label { margin-right: 9px; }
  .person-name { text-transform: uppercase; font-weight: 600; }
  .role-tag {
    display: inline-block;
    margin-left: 12px;
    padding: 0 7px;
    background: var(--white);
    color: var(--brand-red);
    font-size: 12px;
    line-height: 18px;
    border-radius: 9px;
    text-transform: uppercase;
    vertical-align: 1px;
  }
</style>
</head>
<body>

<section class="card card-front" aria-label="Business card front">
  <span class="band band-top"></span>
  <span class="band band-bottom"></span>
  <span class="rule rule-upper"></span>
  <span class="rule rule-lower"></span>

  <div class="brand">
    <span class="brand-square"></span>
    <span class="brand-name">Kestrel Vane<br>Telemark<br>Legal</span>
  </div>

  <ul class="contact-list">
    <li class="contact-item">
      <svg class="contact-icon" viewBox="0 0 24 24" fill="none" stroke="#fff" stroke-width="1.5"><circle cx="12" cy="8" r="4.5"/><path d="M3.5 21v-1.5c0-3 2.5-4.5 8.5-4.5s8.5 1.5 8.5 4.5V21z"/></svg>
      <span><span class="person-name">Boris Telemark</span><span class="role-tag">Partner</span></span>
    </li>
    <li class="contact-item">
      <svg class="contact-icon" viewBox="0 0 24 24" fill="none" stroke="#fff" stroke-width="1.5"><circle cx="12" cy="12" r="10.5"/><path d="M8.5 7l2 2.2-1.2 1.4c.8 1.7 2 2.9 3.6 3.7l1.4-1.2 2.2 2-1.2 1.4c-3.6-.4-7.2-4-7.6-7.6z"/></svg>
      <span><span class="contact-label">Mobile:</span> 0438 715 642</span>
    </li>
    <li class="contact-item">
      <svg class="contact-icon" viewBox="0 0 24 24" fill="none" stroke="#fff" stroke-width="1.5"><rect x="2" y="5" width="20" height="14" rx="1"/><path d="M2 5l10 8 10-8"/></svg>
      <span><span class="contact-label">Email:</span>boris@kvtlaw.co</span>
    </li>
    <li class="contact-item">
      <svg class="contact-icon" viewBox="0 0 24 24" fill="none" stroke="#fff" stroke-width="1.5"><circle cx="12" cy="12" r="10.5"/><ellipse cx="12" cy="12" rx="4.5" ry="10.5"/><path d="M1.5 12h21M3 7h18M3 17h18"/></svg>
      <span><span class="contact-label">Website:</span>www.kvtlaw.co</span>
    </li>
    <li class="contact-item">
      <svg class="contact-icon" viewBox="0 0 24 24" fill="none" stroke="#fff" stroke-width="1.5"><path d="M12 22s-8-7.5-8-13a8 8 0 0 1 16 0c0 5.5-8 13-8 13z"/><circle cx="12" cy="9" r="3.2"/></svg>
      <span>Level 3, 118 Wexbury Street<br>Sydney , NSW 2000</span>
    </li>
  </ul>
</section>

<section class="card card-back" aria-label="Business card back">
  <div class="brand">
    <span class="brand-square"></span>
    <span class="brand-name">Kestrel Vane<br>Telemark<br>Legal</span>
  </div>
</section>

</body>
</html>
```